creating professional text layers for Varnello Product listings images

I need some text added to several images in a professional eye catching way. The text should be legible on desktop and mobile devices. Rough mocks will be provided. You will just need to make them pop and professional. There are 10 images required in total to the selected designer. Below are just 3 of them

```html
<!DOCTYPE html>
<html lang="en">
<head>
<meta charset="utf-8">
<title>Variable Control Speed — Varnello listing</title>
<link href="https://fonts.googleapis.com/css2?family=Oswald:wght@500;600&display=swap" rel="stylesheet">
<style>
  :root {
    --accent: #f7ab1f;
    --text-light: #f6f1e7;
    --backdrop-dark: #0d0b0a;
    --wood: #c99d6c;
    --wood-deep: #9c7246;
    --machine: #d9d3c3;
    --machine-shade: #8d8a82;
  }
  html, body {
    margin: 0;
    padding: 0;
    width: 1200px;
    height: 1200px;
    overflow: hidden;
    background: var(--backdrop-dark);
  }
  .listing-card {
    position: relative;
    width: 1200px;
    height: 1200px;
    overflow: hidden;
    font-family: "Oswald", "Arial Narrow", sans-serif;
    text-transform: uppercase;
  }
  .product-photo {
    position: absolute;
    inset: 0;
    background:
      radial-gradient(ellipse 360px 560px at 210px 640px, var(--machine) 0%, rgba(190,184,170,0.85) 45%, rgba(120,116,108,0) 100%),
      radial-gradient(ellipse 420px 300px at 620px 720px, rgba(140,138,132,0.7) 0%, rgba(80,78,74,0) 100%),
      linear-gradient(180deg, var(--backdrop-dark) 0%, #1a1512 38%, #5a4330 52%, var(--wood-deep) 66%, var(--wood) 82%, #b98d5e 100%);
  }
  .headline {
    position: absolute;
    right: 55px;
    margin: 0;
    line-height: 1;
    font-weight: 600;
    color: var(--accent);
    text-align: right;
    white-space: nowrap;
  }
  .headline--variable { top: 126px; font-size: 117px; letter-spacing: 1px; }
  .headline--control  { top: 228px; font-size: 190px; letter-spacing: -2px; }
  .headline--speed    { top: 391px; font-size: 257px; letter-spacing: -3px; }
  .divider {
    position: absolute;
    top: 655px;
    right: 55px;
    width: 445px;
    height: 6px;
    background: var(--accent);
  }
  .question {
    position: absolute;
    right: 55px;
    top: 688px;
    margin: 0;
    font-size: 85px;
    font-weight: 500;
    line-height: 88px;
    color: var(--text-light);
    text-align: right;
    white-space: nowrap;
  }
  .question span { display: block; }
</style>
</head>
<body>
  <main class="listing-card">
    <div class="product-photo" role="img" aria-label="Photo of a motorized wire stripping machine with speed dial, emergency stop and power switch on a wooden workbench against a dark backdrop"></div>

    <h1 class="headline headline--variable">Variable</h1>
    <p class="headline headline--control">Control</p>
    <p class="headline headline--speed">Speed</p>

    <div class="divider"></div>

    <p class="question">
      <span>How could</span>
      <span>you possibly</span>
      <span>strip all gauges</span>
      <span>at the same</span>
      <span>speed?</span>
    </p>
  </main>
</body>
</html>
```